Business card for Northway's Blue Wagon.

Good day i am looking for a business card design for my business.
The name of the business is Northway's Blue Wagon. It is a van rental business that provides a driver and helper to the customer. Customer have use to van for small moves, studio or 1 bedroom, Moving furniture like couch or kitchen cabinets.
We are available evenings, weekends and holidays.
the means to contact us is by phone at 614-927-3048; By emails at Kestrel@northwaysbluewagon-example.com; or by social media, Chatterly and Snapframe.
You can see attached pictures of the van and or logo.

```html
<!DOCTYPE html>
<html lang="en">
<head>
<meta charset="utf-8">
<title>Northway's Blue Wagon — Business Card</title>
<link rel="stylesheet" href="https://fonts.googleapis.com/css2?family=Merriweather:wght@400;700;900&display=swap">
<style>
  :root {
    --backdrop: #2e2e2f;
    --card-white: #ffffff;
    --ink: #1d1d1f;
    --ink-soft: #3a3a3c;
    --brand-red: #d81f26;
    --photo-red: #c9171d;
    --photo-grey: #a9a9ad;
    --photo-green: #6f8f4a;
    --divider: #6b6b6b;
  }
  * { box-sizing: border-box; margin: 0; padding: 0; }
  html, body {
    width: 1200px; height: 900px; overflow: hidden;
    background: var(--backdrop);
    font-family: "Merriweather", Georgia, serif;
  }
  .canvas { position: relative; width: 1200px; height: 900px; }

  .card {
    position: absolute;
    width: 600px; height: 343px;
    border-radius: 4px;
    overflow: hidden;
    box-shadow: 0 14px 30px rgba(0,0,0,.45);
  }

  /* Front side */
  .card-front { left: 110px; top: 70px; }
  .van-photo {
    position: absolute; inset: 0;
    background:
      linear-gradient(180deg, var(--photo-green) 0%, rgba(111,143,74,0) 22%),
      linear-gradient(160deg, var(--photo-red) 0%, var(--photo-red) 52%, #8e1216 62%, var(--photo-grey) 72%, #c4c4c7 100%);
  }
  .front-service {
    position: absolute; left: 58px; top: 118px;
    color: var(--card-white);
    font-size: 13px; line-height: 1.5; font-weight: 400;
    transform: rotate(-14deg); transform-origin: left top;
  }
  .front-brand {
    position: absolute; right: 26px; bottom: 26px;
    display: flex; align-items: center; gap: 14px;
  }
  .front-brand-name {
    font-size: 13px; font-weight: 700; color: var(--ink);
    max-width: 120px; line-height: 1.3; text-align: right;
  }
  .front-slogan {
    font-size: 21px; font-weight: 900; color: var(--ink);
    line-height: 1.15;
  }

  /* Back side */
  .card-back { left: 490px; top: 480px; background: var(--card-white); }
  .back-slogan {
    position: absolute; top: 26px; left: 0; right: 0;
    text-align: center; font-size: 15px; font-weight: 900; color: var(--ink);
  }
  .back-brand {
    position: absolute; left: 40px; top: 120px; width: 200px;
    display: flex; align-items: center; gap: 10px;
  }
  .brand-dot {
    flex: none; width: 22px; height: 22px; border-radius: 50%;
    background: var(--brand-red);
  }
  .back-brand-name {
    font-size: 20px; font-weight: 700; color: var(--brand-red); line-height: 1.25;
  }
  .back-divider {
    position: absolute; left: 262px; top: 88px; width: 1px; height: 150px;
    background: var(--divider);
  }
  .contact-list {
    position: absolute; left: 282px; top: 92px; right: 16px;
    list-style: none;
  }
  .contact-list li {
    display: flex; align-items: center; gap: 10px; margin-bottom: 14px;
    color: var(--ink-soft);
  }
  .social-row { gap: 16px !important; }
  .social-item { display: flex; align-items: center; gap: 6px; font-size: 11px; }
  .social-dot { width: 20px; height: 20px; border-radius: 50%; background: #4a6fb5; }
  .social-dot.alt { background: #c23d8a; }
  .contact-phone { font-size: 22px; font-weight: 700; letter-spacing: .5px; }
  .contact-email { font-size: 11.5px; font-weight: 700; }
  .contact-icon { flex: none; width: 20px; height: 20px; }
  .back-service {
    position: absolute; bottom: 30px; left: 0; right: 0;
    text-align: center; font-size: 14px; color: var(--ink-soft); letter-spacing: .3px;
  }
</style>
</head>
<body>
<main class="canvas">

  <section class="card card-front" aria-label="Card front">
    <div class="van-photo" role="img" aria-label="Photo of a red cargo van with its side door open, a hand truck and a loading ramp in a driveway"></div>
    <p class="front-service">Van Rental With Driver<br>Evening And Weekends</p>
    <div class="front-brand">
      <span class="front-brand-name">Northway's Blue Wagon</span>
      <p class="front-slogan">Your Friend<br>With The Van</p>
    </div>
  </section>

  <section class="card card-back" aria-label="Card back">
    <p class="back-slogan">Your Friend With The Van</p>
    <div class="back-brand">
      <span class="brand-dot"></span>
      <span class="back-brand-name">Northway's Blue Wagon</span>
    </div>
    <div class="back-divider"></div>
    <ul class="contact-list">
      <li class="social-row">
        <span class="social-item"><span class="social-dot"></span>Chatterly</span>
        <span class="social-item"><span class="social-dot alt"></span>Snapframe</span>
      </li>
      <li>
        <svg class="contact-icon" viewBox="0 0 24 24" aria-hidden="true">
          <path fill="#d81f26" d="M6.6 10.8a15.2 15.2 0 0 0 6.6 6.6l2.2-2.2c.3-.3.7-.4 1-.2 1.1.4 2.3.6 3.6.6.6 0 1 .4 1 1V20c0 .6-.4 1-1 1A17 17 0 0 1 3 4c0-.6.4-1 1-1h3.5c.6 0 1 .4 1 1 0 1.3.2 2.5.6 3.6.1.3 0 .7-.2 1z"/>
        </svg>
        <span class="contact-phone">614-927-3048</span>
      </li>
      <li>
        <svg class="contact-icon" viewBox="0 0 24 24" aria-hidden="true">
          <rect x="2" y="5" width="20" height="14" rx="1.5" fill="#d81f26"/>
          <path d="M3 6.5l9 6.5 9-6.5" fill="none" stroke="#fff" stroke-width="1.6"/>
        </svg>
        <span class="contact-email">Kestrel@northwaysbluewagon-example.com</span>
      </li>
    </ul>
    <p class="back-service">Van Rental With Driver / Evening And Weekends</p>
  </section>

</main>
</body>
</html>
```